Flyer Design & Business Cards

I have tried to make up some flyer and have attached them as info with what we would like included. I would like them made to look more professional and I would like business cards along the same line.

Industry/Entity Type

Business

```html
<!DOCTYPE html>
<html lang="en">
<head>
<meta charset="utf-8">
<title>Harbourne Inn – Business Cards</title>
<link rel="stylesheet" href="https://fonts.googleapis.com/css2?family=Nunito+Sans:wght@400;600;700;800&display=swap">
<style>
  :root {
    --page-bg: #ececec;
    --card-blue: #175f87;
    --gold: #f6ad3d;
    --gold-glow: rgba(246, 173, 61, 0.55);
    --silver-glow: rgba(214, 224, 232, 0.5);
    --gold-shade: #bf7f22;
    --ink-blue: #1c5d86;
    --white: #ffffff;
  }
  * { margin: 0; padding: 0; box-sizing: border-box; }
  html, body { width: 1200px; height: 1200px; overflow: hidden; }
  body {
    background: var(--page-bg);
    font-family: "Nunito Sans", Arial, sans-serif;
    position: relative;
  }
  .card {
    position: absolute;
    left: 187px;
    width: 840px;
    height: 480px;
    overflow: hidden;
    background: var(--card-blue);
  }
  .card--front { top: 98px; }
  .card--back { top: 618px; }

  .card__photo {
    position: absolute; inset: 0;
    background: linear-gradient(180deg, #1d6a93 0%, #135a82 45%, #0f5479 100%);
  }

  .corner {
    position: absolute;
    width: 104px; height: 108px;
  }
  .corner--tl { left: 22px; top: 20px; }
  .corner--tr { right: 22px; top: 20px; }
  .corner--bl { left: 22px; bottom: 22px; }
  .corner--br { right: 22px; bottom: 22px; }
  .corner--gold.corner--tl { background: radial-gradient(circle at 0 0, var(--gold-glow) 0%, rgba(246,173,61,0) 70%); }
  .corner--gold.corner--br { background: radial-gradient(circle at 100% 100%, var(--gold-glow) 0%, rgba(246,173,61,0) 70%); }
  .corner--silver.corner--tr { background: radial-gradient(circle at 100% 0, var(--silver-glow) 0%, rgba(214,224,232,0) 70%); }
  .corner--silver.corner--bl { background: radial-gradient(circle at 0 100%, var(--silver-glow) 0%, rgba(214,224,232,0) 70%); }

  .brand {
    position: absolute;
    color: var(--gold);
    font-weight: 800;
    text-align: center;
    line-height: 1;
    letter-spacing: 1px;
  }
  .brand__line { display: block; }
  .brand__line + .brand__line { margin-top: 6px; }
  .card--front .brand { left: 0; right: 0; top: 196px; font-size: 58px; }
  .card--back .brand { left: 71px; width: 300px; top: 236px; font-size: 50px; }

  .ribbon { position: absolute; left: 149px; top: 341px; width: 544px; height: 98px; }
  .ribbon__text {
    position: absolute; left: 53px; top: 7px; width: 436px; height: 66px;
    display: flex; align-items: center; justify-content: center;
    color: var(--ink-blue);
    font-size: 27px; font-weight: 600;
    letter-spacing: -0.3px;
    text-transform: uppercase;
  }

  .contact { position: absolute; left: 420px; top: 130px; width: 380px; color: var(--white); }
  .contact__row { display: flex; align-items: flex-start; gap: 10px; }
  .contact__icon { width: 24px; height: 24px; flex: none; margin-top: 4px; }
  .contact__text { font-size: 24px; line-height: 33px; }
  .contact__row--phone .contact__text { font-weight: 800; letter-spacing: 0.5px; }
  .contact__row--web { margin-top: 8px; }
  .contact__row--address { margin-top: 10px; }
  .contact__rule { margin: 12px 0 0 34px; height: 1px; background: var(--gold); width: 336px; }
  .social { display: flex; gap: 11px; margin: 19px 0 0 32px; }
  .social__link {
    width: 50px; height: 50px; border-radius: 50%;
    background: var(--white);
    display: flex; align-items: center; justify-content: center;
    color: var(--ink-blue);
    font-size: 12px; font-weight: 800;
  }
</style>
</head>
<body>

<section class="card card--front">
  <div class="card__photo" role="img" aria-label="Faded photograph of the inn building by the water"></div>
  <div class="corner corner--gold corner--tl" role="img" aria-label="Gold scroll ornament"></div>
  <div class="corner corner--silver corner--tr" role="img" aria-label="Silver scroll ornament"></div>
  <div class="corner corner--silver corner--bl" role="img" aria-label="Silver scroll ornament"></div>
  <div class="corner corner--gold corner--br" role="img" aria-label="Gold scroll ornament"></div>

  <h1 class="brand"><span class="brand__line">Harbourne</span><span class="brand__line">Inn</span></h1>

  <div class="ribbon">
    <svg width="544" height="98" viewBox="0 0 544 98" aria-hidden="true">
      <polygon points="0,38 64,38 64,97 0,97 30,68" fill="var(--gold)"/>
      <polygon points="544,38 480,38 480,97 544,97 514,68" fill="var(--gold)"/>
      <polygon points="6,42 58,42 58,93 8,93 36,68" fill="none" stroke="var(--white)" stroke-width="2"/>
      <polygon points="538,42 486,42 486,93 536,93 508,68" fill="none" stroke="var(--white)" stroke-width="2"/>
      <polygon points="53,79 153,79 153,97 64,97" fill="var(--gold-shade)"/>
      <polygon points="491,79 391,79 391,97 480,97" fill="var(--gold-shade)"/>
      <rect x="53" y="0" width="438" height="80" fill="var(--gold)"/>
      <rect x="62" y="7" width="420" height="66" fill="none" stroke="var(--white)" stroke-width="2"/>
    </svg>
    <div class="ribbon__text">The only pub in North Isle</div>
  </div>
</section>

<section class="card card--back">
  <div class="card__photo" role="img" aria-label="Faded photograph of the inn and its sign"></div>
  <div class="corner corner--gold corner--tl" role="img" aria-label="Gold scroll ornament"></div>
  <div class="corner corner--silver corner--tr" role="img" aria-label="Silver scroll ornament"></div>
  <div class="corner corner--silver corner--bl" role="img" aria-label="Silver scroll ornament"></div>
  <div class="corner corner--gold corner--br" role="img" aria-label="Gold scroll ornament"></div>

  <h2 class="brand"><span class="brand__line">Harbourne</span><span class="brand__line">Inn</span></h2>

  <div class="contact">
    <div class="contact__row contact__row--phone">
      <svg class="contact__icon" viewBox="0 0 24 24" aria-hidden="true"><path d="M6.5 2.5l3 3.5-2 2.2c1.2 2.8 3.4 5 6.3 6.3l2.2-2 3.5 3-1.8 3c-7.4.2-13.7-6.1-13.5-13.5z" fill="none" stroke="var(--white)" stroke-width="1.8" stroke-linejoin="round"/><path d="M14 3a7 7 0 0 1 7 7M14 6.5a3.5 3.5 0 0 1 3.5 3.5" fill="none" stroke="var(--white)" stroke-width="1.6" stroke-linecap="round"/></svg>
      <span class="contact__text">01632 960417</span>
    </div>
    <div class="contact__row contact__row--web">
      <svg class="contact__icon" viewBox="0 0 24 24" aria-hidden="true"><g fill="none" stroke="var(--white)" stroke-width="1.5"><circle cx="12" cy="12" r="9.5"/><ellipse cx="12" cy="12" rx="4" ry="9.5"/><path d="M2.5 12h19M4 7h16M4 17h16"/></g></svg>
      <span class="contact__text">www.harbourneinn.com</span>
    </div>
    <div class="contact__row contact__row--address">
      <svg class="contact__icon" viewBox="0 0 24 24" aria-hidden="true"><g fill="none" stroke="var(--white)" stroke-width="1.7"><path d="M12 21s-6-6.5-6-11a6 6 0 0 1 12 0c0 4.5-6 11-6 11z"/><circle cx="12" cy="10" r="2.3"/><path d="M5 21h14" stroke-linecap="round"/></g></svg>
      <span class="contact__text">Harbourne Inn, Shore Road<br>Kilbrannan, North Isle HS9 4ZQ</span>
    </div>
    <div class="contact__rule"></div>
    <div class="social">
      <span class="social__link">Kith</span>
      <span class="social__link">Chirp</span>
    </div>
  </div>
</section>

</body>
</html>
```